SkyvoraQ Business Cards and Stationary Design

Need a design for our business cards and stationary. I want to carry on the theme of the logo. I want the business cards to have a design on the back. I would like the business cards and the stationary to carry the same theme, design scheme, and branding

Target Market(s)

Airlines and Maintenance Facilities

Industry/Entity Type

Aviation

Contact Information for Business Card

Name
Position Title
Address: 4827 Tollbeck Lane, Fort Pierce, Florida, 34951
Office Number
Mobile Number
Email
Website

Font styles to use
Serif
Sans Serif

Colors

Designer to choose colors to be used in the design.

```html
<!DOCTYPE html>
<html lang="en">
<head>
<meta charset="utf-8">
<title>SkyvoraQ Business Card</title>
<link rel="stylesheet" href="https://fonts.googleapis.com/css2?family=Montserrat:wght@500&family=Work+Sans:wght@400;600;700&display=swap">
<style>
  :root {
    --navy: #142a56;
    --navy-soft: #1d3768;
    --white: #ffffff;
    --ink: #2f3238;
    --page: #1e1e1f;
    --card-sheen: #e4e4e6;
  }
  * { margin: 0; padding: 0; box-sizing: border-box; }
  html, body { width: 1200px; height: 897px; overflow: hidden; background: var(--page); }
  .canvas { position: relative; width: 1200px; height: 897px; }

  .card {
    position: absolute;
    left: 347px;
    width: 499px;
    height: 284px;
    border-radius: 14px;
    overflow: hidden;
  }

  /* Front */
  .card-front {
    top: 158px;
    background: radial-gradient(circle at 50% 55%, var(--navy-soft) 0%, var(--navy) 70%);
  }
  .brand-mark {
    position: absolute;
    left: 50%;
    top: 58px;
    width: 92px;
    height: 92px;
    margin-left: -46px;
    border: 5px solid var(--white);
    border-radius: 50%;
  }
  .brand-name {
    position: absolute;
    left: 0; right: 0;
    top: 162px;
    text-align: center;
    font-family: "Work Sans", sans-serif;
    font-weight: 700;
    font-size: 36px;
    line-height: 44px;
    letter-spacing: 5px;
    color: var(--white);
    white-space: nowrap;
  }
  .front-web {
    position: absolute;
    left: 0; right: 0;
    top: 243px;
    text-align: center;
    font-family: "Work Sans", sans-serif;
    font-weight: 600;
    font-size: 13px;
    color: var(--white);
  }

  /* Back */
  .card-back {
    top: 465px;
    background: radial-gradient(circle at 92% 5%, var(--card-sheen) 0%, var(--white) 55%);
  }
  .name-band {
    position: absolute;
    left: 0; top: 27px;
    width: 249px; height: 57px;
    background: var(--navy);
    border-radius: 0 29px 29px 0;
    color: var(--white);
    padding-left: 25px;
    white-space: nowrap;
  }
  .person-name {
    font-family: "Montserrat", sans-serif;
    font-weight: 500;
    font-size: 23px;
    line-height: 24px;
    padding-top: 8px;
    letter-spacing: 0.2px;
  }
  .person-title {
    font-family: "Work Sans", sans-serif;
    font-size: 13.5px;
    line-height: 16px;
    margin-top: 1px;
    letter-spacing: 0.4px;
  }
  .address {
    position: absolute;
    left: 25px; top: 115px;
    font-family: "Work Sans", sans-serif;
    font-style: normal;
    font-size: 11.5px;
    line-height: 15.5px;
    color: var(--ink);
    letter-spacing: 0.3px;
  }
  .contacts {
    position: absolute;
    left: 25px; top: 187px;
    list-style: none;
    font-family: "Work Sans", sans-serif;
    font-size: 12.5px;
    line-height: 16.2px;
    color: var(--ink);
    white-space: nowrap;
  }
  .contacts li { display: flex; align-items: center; }
  .contacts svg { width: 9px; height: 9px; margin-right: 13px; fill: none; stroke: var(--navy); stroke-width: 1.6; flex: none; }
  .contacts strong { color: var(--navy); font-weight: 600; }
</style>
</head>
<body>
<div class="canvas">
  <section class="card card-front">
    <div class="brand-mark"></div>
    <div class="brand-name">SKYVORAQ</div>
    <div class="front-web">www.skyvoraq.com</div>
  </section>

  <section class="card card-back">
    <div class="name-band">
      <div class="person-name">DANA WHITLOCK</div>
      <div class="person-title">Co-Owner</div>
    </div>
    <address class="address">
      4827 Tollbeck Lane,<br>Fort Pierce,<br>Florida, 34951
    </address>
    <ul class="contacts">
      <li><svg viewBox="0 0 10 10"><rect x="2.5" y="0.8" width="5" height="8.4" rx="1"/></svg>(555) 318-4072</li>
      <li><svg viewBox="0 0 10 10"><path d="M2 1 L4 1 L4.6 3.2 L3.4 4 Q4.5 6 6 6.6 L6.8 5.4 L9 6 L9 8 Q4 9 1 3 Z"/></svg>1-800-555-0147 (Toll Free)</li>
      <li><svg viewBox="0 0 10 10"><rect x="0.8" y="2" width="8.4" height="6"/><path d="M0.8 2 L5 5.5 L9.2 2"/></svg>info@skyvoraq.com</li>
      <li><svg viewBox="0 0 10 10"><circle cx="5" cy="5" r="4.2"/><path d="M0.8 5 H9.2 M5 0.8 Q2 5 5 9.2 M5 0.8 Q8 5 5 9.2"/></svg>www.<strong>skyvoraq</strong>.com</li>
    </ul>
  </section>
</div>
</body>
</html>
```